Business Cards for a Junk Removal Company

Hello,
We are looking to have business cards designed that are simple, bold, easy to read, and right to the point. Please see the attachments for our logo files. We want the card to be yellow on both sides ( Color code Yellow: #FFE01B). The logo text font is (Rockstar Extra Bold) and this is also in the files attached. Please make the text black for the logo. On the back side of the card, you can use white and black for text. Thank you in advance for your hard work!

Front of card-
Harbor Haul Away (logo)
Back of card-
Harbor Haul Away
Donate - Recycle - Dispose
555-271-8093
www.harborhaulaway.example
info@harborhaulaway.example

Industry/Entity Type

Junk removal

Contact Information for Business Card

FRONT OF CARD- Harbor Haul Away (logo) BACK OF CARD- Harbor Haul Away Donate - Recycle - Dispose 555-271-8093 www.harborhaulaway.example info@harborhaulaway.example

Font styles to use
Other font styles liked:
• Rockstar Extra Bold

Colors
FFF300
FFF600
FEFA6F
FFFEC7
FFFEE8

Requirements
Must have
• Must have color code Yellow: #FFE01B for the background of front and back of the card

```html
<!DOCTYPE html>
<html lang="en">
<head>
<meta charset="utf-8">
<title>Harbor Haul Away – Business Cards</title>
<link href="https://fonts.googleapis.com/css2?family=Archivo+Black&family=Oswald:wght@300;400&display=swap" rel="stylesheet">
<style>
  :root {
    --yellow: #FFE01B;
    --ink: #0a0a0a;
    --paper-white: #ffffff;
    --backdrop: #3a3a3a;
    --divider: rgba(0,0,0,0.35);
  }
  * { margin: 0; padding: 0; box-sizing: border-box; }
  html, body {
    width: 1200px; height: 1200px; overflow: hidden;
    background: var(--backdrop);
  }
  .canvas {
    position: relative; width: 1200px; height: 1200px;
  }
  .card {
    position: absolute; left: 220px;
    width: 760px; height: 434px;
    background: var(--yellow);
    border-radius: 34px;
    overflow: hidden;
    color: var(--ink);
  }
  .card--back { top: 130px; }
  .card--front { top: 636px; }

  /* back side */
  .brand-small {
    position: absolute; left: 60px; top: 120px; width: 250px;
    font-family: "Archivo Black", sans-serif;
    font-size: 40px; line-height: 1.02; text-transform: uppercase;
    color: var(--ink);
  }
  .divider {
    position: absolute; left: 345px; top: 70px;
    width: 1px; height: 190px; background: var(--divider);
  }
  .contact {
    position: absolute; left: 385px; top: 62px;
  }
  .contact__name {
    font-family: "Archivo Black", sans-serif;
    font-size: 40px; line-height: 1; text-transform: uppercase;
  }
  .contact__role {
    font-family: "Oswald", sans-serif; font-weight: 300;
    font-size: 22px; letter-spacing: 1px; text-transform: uppercase;
    margin-bottom: 14px;
  }
  .contact__list { list-style: none; }
  .contact__item {
    display: flex; align-items: center; gap: 12px;
    font-family: "Oswald", sans-serif; font-weight: 400;
    font-size: 21px; text-transform: uppercase; line-height: 1.6;
  }
  .contact__icon { width: 22px; height: 22px; flex: none; }
  .tagline-band {
    position: absolute; left: 0; right: 0; top: 318px; height: 52px;
    background: var(--ink);
    display: flex; align-items: center; justify-content: flex-end;
    padding-right: 60px;
    font-family: "Archivo Black", sans-serif;
    font-size: 27px; letter-spacing: 1px; text-transform: uppercase;
    color: var(--paper-white);
  }

  /* front side */
  .brand-large {
    position: absolute; inset: 0;
    display: flex; align-items: center; justify-content: center;
    text-align: center;
    font-family: "Archivo Black", sans-serif;
    font-size: 82px; line-height: 1.02; text-transform: uppercase;
    color: var(--ink);
  }
</style>
</head>
<body>
<main class="canvas">

  <section class="card card--back" aria-label="Card back">
    <div class="brand-small">Harbor Haul Away</div>
    <div class="divider"></div>
    <div class="contact">
      <p class="contact__name">Sam Rivera</p>
      <p class="contact__role">Owner</p>
      <ul class="contact__list">
        <li class="contact__item">
          <svg class="contact__icon" viewBox="0 0 24 24" aria-hidden="true"><path fill="currentColor" d="M6.6 10.8a15 15 0 0 0 6.6 6.6l2.2-2.2a1 1 0 0 1 1-.25 11.4 11.4 0 0 0 3.6.57 1 1 0 0 1 1 1V20a1 1 0 0 1-1 1A17 17 0 0 1 3 4a1 1 0 0 1 1-1h3.5a1 1 0 0 1 1 1c0 1.25.2 2.45.57 3.57a1 1 0 0 1-.25 1z"/></svg>
          555-271-8093
        </li>
        <li class="contact__item">
          <svg class="contact__icon" viewBox="0 0 24 24" aria-hidden="true"><path fill="currentColor" d="M2 5h20v14H2zm2 2v.5l8 5 8-5V7zm0 2.8V17h16V9.8l-8 5z"/></svg>
          info@harborhaulaway.example
        </li>
        <li class="contact__item">
          <svg class="contact__icon" viewBox="0 0 24 24" aria-hidden="true"><g fill="none" stroke="currentColor" stroke-width="1.8"><circle cx="12" cy="12" r="9.5"/><ellipse cx="12" cy="12" rx="4" ry="9.5"/><path d="M2.5 12h19M4 7h16M4 17h16"/></g></svg>
          www.harborhaulaway.example
        </li>
      </ul>
    </div>
    <div class="tagline-band">Donate - Recycle - Dispose</div>
  </section>

  <section class="card card--front" aria-label="Card front">
    <div class="brand-large">Harbor<br>Haul Away</div>
  </section>

</main>
</body>
</html>
```